Poster for Office

Looking for an edgy, beautiful poster to hang up in my office that uses the quotes located below and potentially the image attached.
Content for poster

Title: Pell's Rules

Must have the following quotes included (punctuation and capitalization are flexible, do what you think looks the best they also don't need the quotation symbols):

"Don't order fish at a steakhouse"
"Be bold. The more you tell, the more you sell"
"admit nothing, deny everything, launch counterattack."
"avoid obviousness"
"never do anything until you're ready to do it"
"look good=feel good"
"always keep the advantage"
"never complain, never explain"
"Lay low, play dumb, keep moving"

Industry/Entity Type

Quotes

Requirements
Must have
• Title: Pell's Rules

"avoid obviousness"
"look good=feel good"

```html
<!DOCTYPE html>
<html lang="en">
<head>
<meta charset="utf-8">
<title>Pell's Rules</title>
<link rel="stylesheet" href="https://fonts.googleapis.com/css2?family=Poppins:wght@600;700&display=swap">
<style>
  :root {
    --paper: #ffffff;
    --title: rgba(120, 100, 98, 0.82);
    --ink: #111111;
    --green: rgba(96, 178, 88, 0.55);
    --blue: rgba(70, 140, 200, 0.55);
    --red: rgba(214, 80, 60, 0.6);
    --yellow: rgba(240, 220, 80, 0.5);
  }
  * { margin: 0; padding: 0; box-sizing: border-box; }
  html, body { width: 848px; height: 1200px; overflow: hidden; background: var(--paper); }
  .poster {
    position: relative;
    width: 848px;
    height: 1200px;
    overflow: hidden;
    background: var(--paper);
    font-family: "Poppins", "Century Gothic", sans-serif;
  }
  .portrait-art {
    position: absolute;
    left: 110px;
    top: 0;
    width: 738px;
    height: 1180px;
    background:
      radial-gradient(ellipse 260px 360px at 330px 400px, rgba(214, 90, 60, 0.55), transparent 70%),
      linear-gradient(125deg,
        transparent 8%,
        var(--green) 18%,
        var(--yellow) 28%,
        var(--blue) 38%,
        var(--red) 50%,
        var(--blue) 62%,
        var(--green) 74%,
        transparent 90%);
    -webkit-mask-image: linear-gradient(200deg, #000 55%, transparent 95%);
            mask-image: linear-gradient(200deg, #000 55%, transparent 95%);
  }
  .title-block { font-size: 0; }
  .title {
    position: absolute;
    color: var(--title);
    font-weight: 700;
    letter-spacing: -2px;
    line-height: 1;
    white-space: nowrap;
  }
  .title-name { left: 0; top: -43px; font-size: 300px; }
  .title-rules { left: 130px; top: 298px; font-size: 245px; }
  .rules-list {
    position: absolute;
    left: 243px;
    top: 522px;
    list-style: none;
    transform-origin: 0 0;
    transform: rotate(35deg);
    color: var(--ink);
    font-size: 24px;
    font-weight: 700;
    line-height: 37px;
    white-space: nowrap;
  }
  .rules-list li { margin-left: calc(var(--i) * -8px); }
</style>
</head>
<body>
  <main class="poster">
    <div class="portrait-art" role="img" aria-label="Smiling man's portrait in sepia red, overlaid with diagonal streaks of green, yellow, blue and red light"></div>
    <h1 class="title-block">
      <span class="title title-name">Pell's</span>
      <span class="title title-rules">Rules</span>
    </h1>
    <ul class="rules-list">
      <li style="--i:0">Don't order fish at a steakhouse.</li>
      <li style="--i:1">Be bold. The more you tell, the more you sell.</li>
      <li style="--i:2">Admit nothing, deny everything, launch counterattack.</li>
      <li style="--i:3">Avoid obviousness.</li>
      <li style="--i:4">Never do anything until you're ready to do it.</li>
      <li style="--i:5">Look good=feel good.</li>
      <li style="--i:6">Always keep the advantage.</li>
      <li style="--i:7">Never complain, never explain.</li>
      <li style="--i:8">Lay low, play dumb, keep moving.</li>
    </ul>
  </main>
</body>
</html>
```